Wordpress Website for electrician

I'm looking for an easy to maintain website for my electrical contracting business. Need a professional and appealing site.
Im wanting a website where clients can come on and look at services we offer, case studies and advertise our services.
Colours I'm wanting to incorporate are green, white, black and grey
I'm wanting a big slide show on main page where I can place advertising etc.
Menu is to include home, services, our work, specials, energy efficiency and contact
My existing site is www.trelwirefix.com.au
Updates
looking for something with a similar layout to this website
Target Market(s)
Businesses
Industry/Entity Type
Electrician
Look and feel

```html
<!DOCTYPE html>
<html lang="en">
<head>
<meta charset="utf-8">
<title>trelwirefix – Electrical Contracting</title>
<link href="https://fonts.googleapis.com/css2?family=Arimo:wght@400;700&family=Open+Sans:ital,wght@0,300;0,400;1,600&family=PT+Sans&display=swap" rel="stylesheet">
<style>
:root{
  --green:#2e9a3a;
  --green-dark:#1d7a25;
  --black:#000;
  --panel:#151515;
  --white:#fff;
  --grey:#bdbdbd;
  --grey-light:#e8e8e8;
  --card:#eeeeee;
  --red:#c8202a;
  --text:#222;
}
*{margin:0;padding:0;box-sizing:border-box}
html,body{width:1188px;height:1200px;overflow:hidden;background:var(--black)}
body{position:relative;font-family:"Arimo",Arial,sans-serif;color:var(--white)}
.abs{position:absolute}

/* header */
.site-header{left:0;top:0;width:1188px;height:98px;background:var(--white)}
.brand{left:12px;top:26px;display:flex;align-items:center;gap:12px}
.brand-dot{width:34px;height:34px;border-radius:50%;background:var(--green)}
.brand-name{font-family:"Arimo",sans-serif;font-weight:700;font-size:34px;color:var(--text);letter-spacing:.5px}
.main-nav{right:30px;top:34px;display:flex;gap:0}
.main-nav a{color:#111;text-decoration:none;font-size:17px;padding:5px 12px;margin-left:10px}
.main-nav a.active{background:#111;color:var(--white)}

/* hero */
.hero{left:0;top:98px;width:1188px;height:298px;
  background:linear-gradient(180deg,#3c4a68 0%,#6a6f86 35%,#a77a5a 62%,#e0703a 75%,#3a2a22 88%,#1b1a18 100%)}
.hero-band{left:600px;top:215px;width:588px;height:150px;background:rgba(70,72,80,.55)}
.hero-title{right:20px;top:222px;font-family:"Open Sans",sans-serif;font-weight:300;font-size:86px;line-height:1}
.hero-sub{right:22px;top:320px;font-family:"Open Sans",sans-serif;font-size:21px;color:#eee}
.hero-quote{left:80px;top:364px;font-family:"Open Sans",sans-serif;font-style:italic;font-weight:600;font-size:18px;color:#ddd}
.hero-pager{right:20px;top:372px;display:flex;gap:20px;font-weight:700;font-size:16px}
.hero-rule{left:0;top:396px;width:1188px;height:2px;background:var(--green)}

/* feature cards */
.card{top:455px;height:154px;border:3px solid var(--white);border-radius:3px;overflow:hidden}
.card-services{left:40px;width:351px;background:linear-gradient(135deg,#6b3d22,#a8704a 50%,#4a2a18)}
.card-offer{left:421px;width:350px;background:linear-gradient(180deg,#8fb3d6,#b9c6cf 45%,#4b5a3c)}
.card-news{left:804px;width:355px;background:linear-gradient(135deg,#1e2a44,#33415e 60%,#0f1525)}
.card-label{position:absolute;left:0;bottom:18px;width:230px;padding:8px 12px;background:rgba(0,0,0,.45)}
.card-label h3{font-weight:400;font-size:21px}
.card-label a{color:var(--white);font-size:14px}
.news-title{position:absolute;left:13px;top:6px;font-size:21px}
.news-list{position:absolute;left:22px;top:38px;list-style:none}
.news-list li{font-size:14px;border-bottom:1px solid var(--white);margin-bottom:9px;padding-bottom:1px}

/* intro row */
.intro-rule{left:0;top:645px;width:1188px;height:1px;background:#333}
.intro-name{left:60px;top:662px;font-size:28px;font-weight:700;line-height:1.2}
.intro-text{left:224px;top:662px;width:560px;font-size:14px;line-height:1.45;color:#ddd}
.intro-text p+p{margin-top:19px}
.intro-more{left:646px;top:746px;font-size:17px}
.social-divider{left:798px;top:675px;width:1px;height:54px;background:#333}
.social{top:682px;width:52px;height:42px;border-radius:3px;background:linear-gradient(#5a5a5a,#2a2a2a)}
.intro-strip{left:0;top:779px;width:1188px;height:13px;background:var(--grey-light)}

/* footer */
.site-footer{left:0;top:792px;width:1188px;height:374px;background:var(--panel);border:1px solid var(--green)}
.footer-heading{font-family:"PT Sans",sans-serif;font-size:25px;color:#ddd}
.footer-list{list-style:none;font-size:16px;color:#bbb}
.footer-list li{height:35px;line-height:34px;border-bottom:1px solid #2e2e2e;padding-left:32px;position:relative}
.footer-list li::before{content:"·";position:absolute;left:12px;color:#888}
.footer-list li.current{color:var(--white)}
.contact-icon{left:800px;top:816px;width:44px;height:44px;border-radius:4px;background:linear-gradient(#5a8a3a,#2c4a20)}
.contact-heading{left:858px;top:822px;font-family:"PT Sans",sans-serif;font-size:27px;letter-spacing:2px;color:#ddd}
.contact-card{left:814px;top:872px;width:268px;height:208px;background:var(--card);border-radius:8px;color:var(--text);padding:12px 20px}
.contact-card h4{color:var(--red);font-size:14px;font-weight:400;margin-bottom:1px}
.contact-card p{font-size:13px;color:#444;line-height:1.35}
.contact-card p b{color:#333}
.contact-card .gap{margin-top:18px}
.email-link{display:flex;align-items:center;gap:8px;margin-top:24px}
.email-link span.icon{width:30px;height:30px;border-radius:50%;background:var(--red)}
.email-link span.txt{font-size:9px;font-weight:700;line-height:1.1;color:#555}
.email-link span.txt em{font-style:normal;color:var(--red);display:block}
.copyright{left:0;top:1114px;width:1000px;text-align:center;font-size:12px;color:#ddd}
.bottom-band{left:0;top:1166px;width:1188px;height:34px;background:var(--green-dark)}
</style>
</head>
<body>

<header class="site-header abs">
  <div class="brand abs"><span class="brand-dot"></span><span class="brand-name">trelwirefix</span></div>
  <nav class="main-nav abs">
    <a class="active" href="#">Home</a><a href="#">Services</a><a href="#">Our Work</a><a href="#">Specials</a><a href="#">energy efficiency</a><a href="#">Contact</a>
  </nav>
</header>

<section class="hero abs" role="img" aria-label="Slideshow photo: transmission towers and power lines against a sunset sky"></section>
<div class="hero-band abs"></div>
<h1 class="hero-title abs">Power</h1>
<p class="hero-sub abs">Generation, Transmission, Distribution, Metering &amp; Energy Efficiency</p>
<p class="hero-quote abs">“Life is the art of drawing without an eraser.”</p>
<div class="hero-pager abs"><span>1</span><span>2</span><span>3</span></div>
<div class="hero-rule abs"></div>

<article class="card card-services abs" role="img" aria-label="Photo of heavy mining machinery">
  <div class="card-label"><h3>services</h3><a href="#">view the entire series</a></div>
</article>
<article class="card card-offer abs" role="img" aria-label="Photo of an electrician in a hard hat above a city skyline">
  <div class="card-label"><h3>We offer</h3><a href="#">view the entire series</a></div>
</article>
<article class="card card-news abs">
  <h3 class="news-title">News</h3>
  <ul class="news-list">
    <li>Lorem Ipsum is simply dummy text</li>
    <li>Lorem Ipsum is simply dummy text</li>
    <li>Lorem Ipsum is simply dummy text</li>
    <li>Lorem Ipsum is simply dummy text</li>
  </ul>
</article>

<div class="intro-rule abs"></div>
<h2 class="intro-name abs">Halloran<br>Brent</h2>
<div class="intro-text abs">
  <p>Lorem Ipsum is simply dummy text of the printing and typesetting industry. Lorem Ipsum has been the industry's standard dummy text ever since the 1500s,</p>
  <p>Lorem Ipsum is simply dummy text of the printing and typesetting industry.</p>
</div>
<a class="intro-more abs" style="color:var(--white);text-decoration:none" href="#">Read More..</a>
<div class="social-divider abs"></div>
<span class="social abs" style="left:857px"></span>
<span class="social abs" style="left:933px"></span>
<span class="social abs" style="left:1010px"></span>
<span class="social abs" style="left:1086px"></span>
<div class="intro-strip abs"></div>

<footer class="site-footer abs"></footer>
<h3 class="footer-heading abs" style="left:56px;top:824px">Overview</h3>
<ul class="footer-list abs" style="left:40px;top:870px;width:290px">
  <li class="current">Home</li><li>Services</li><li>Our Work</li><li>Specials</li><li>Energy Efficiency</li><li>Contact&nbsp; Us</li>
</ul>
<h3 class="footer-heading abs" style="left:416px;top:826px">Testimonials</h3>
<ul class="footer-list abs" style="left:418px;top:878px;width:290px">
  <li>Lorem Ipsum</li><li>Lorem Ipsum</li><li>Lorem Ipsum</li><li>Lorem Ipsum</li><li>Lorem Ipsum</li>
</ul>
<span class="contact-icon abs"></span>
<h3 class="contact-heading abs">CONTACT US</h3>
<div class="contact-card abs">
  <h4>SALES</h4>
  <p><b>Australia</b> 7 3100 5200</p>
  <h4 class="gap">SALES &amp; SERVICE</h4>
  <p><b>Australia</b> 1300 555 210<br><b>New Zealand</b> 0800 555 319</p>
  <div class="email-link"><span class="icon"></span><span class="txt">EMAIL<em>ENQUIRY FORM</em></span></div>
</div>
<p class="copyright abs">Copyright@2013kestrelweb.com | All right reserved.</p>
<div class="bottom-band abs"></div>

</body>
</html>
```